60 Ways to de-stress Poster

I would like a poster ( A4 full colour) with a list of 60 ways to destress. I would like the design to be clean and stylish (not cartoonish)

My Target market is stressed out mums so I want the poster to feel inspirational and relaxing to look at.

I have added a sample of something I like - but open to other ideas

Finished art would be print ready pdf

Target Market(s)

Mums who are stressed out - mainly new mums. I want this to be a poster that someone would happily put up that looks more like artwork.

Requirements
Must have
• My logo elements and colours but happy to incorporate other colours that blend well into it.

Colours:
Bright green: Pantone 376
Bright green as CMYK: c: 45.2% m: 0% y: 100% k: 0%

Logo text large grey: 70% black
Logo text strapline: 75% black
Tree: 80% black

Fonts:
Logo 'Willowbank Haven': Verdana
Logo 'Counselling & coaching services for mums': Gill Sans Light
Should not have
• No cartoonish images - I want it very clean and stylish

```html
<!DOCTYPE html>
<html lang="en">
<head>
<meta charset="utf-8">
<title>60 Ways to De-stress – Willowbank Haven</title>
<link rel="stylesheet" href="https://fonts.googleapis.com/css2?family=Playfair+Display:ital,wght@1,400&family=Roboto+Condensed:wght@300;400;600&display=swap">
<style>
  :root {
    --sky-top: #0a5aa6;
    --sky-mid: #3f93d4;
    --sky-low: #b9dcf2;
    --sky-horizon: #e4f2fb;
    --grass-light: #8cc83f;
    --grass-mid: #5fa52b;
    --grass-dark: #2f7a17;
    --text-light: #ffffff;
    --brand-grey: #58595b;
    --strap-grey: #4d4d4f;
    --brand-green: #7ab929;
    --frame: #d4d7da;
    --portrait-warm: #5a3b2c;
    --portrait-denim: #4a6a92;
    --tree-green: #4d8a26;
  }
  * { box-sizing: border-box; margin: 0; padding: 0; }
  html, body { width: 850px; height: 1200px; overflow: hidden; background: #fff; }
  .poster {
    position: relative;
    width: 850px;
    height: 1200px;
    overflow: hidden;
    border: 2px solid var(--frame);
    font-family: "Roboto Condensed", "Arial Narrow", sans-serif;
  }
  .scenery { position: absolute; inset: 0; width: 100%; height: 100%; }
  .title {
    position: absolute;
    top: 52px;
    left: 0;
    width: 100%;
    text-align: center;
    font-family: "Playfair Display", Georgia, serif;
    font-style: italic;
    font-weight: 400;
    font-size: 82px;
    letter-spacing: 1px;
    color: var(--text-light);
  }
  .ways {
    position: absolute;
    top: 176px;
    list-style: none;
    color: var(--text-light);
    font-size: 15.5px;
    font-weight: 400;
    line-height: 27.35px;
  }
  .ways li { position: relative; padding-left: 19px; white-space: nowrap; }
  .ways li::before {
    content: "";
    position: absolute;
    left: 0;
    top: 11px;
    width: 6px;
    height: 6px;
    border-radius: 50%;
    background: var(--text-light);
  }
  .ways--first { left: 66px; }
  .ways--second { left: 301px; }
  .ways--third { left: 559px; }
  .brand {
    position: absolute;
    left: 302px;
    top: 838px;
    width: 300px;
  }
  .brand__mark {
    position: absolute;
    left: 228px;
    top: 0;
    width: 62px;
    height: 62px;
    border-radius: 50%;
    background: var(--brand-grey);
  }
  .brand__name {
    position: absolute;
    top: 52px;
    left: 0;
    font-size: 29px;
    font-weight: 600;
    color: var(--brand-grey);
    white-space: nowrap;
  }
  .brand__strap {
    position: absolute;
    top: 88px;
    left: 1px;
    font-size: 15px;
    font-weight: 300;
    color: var(--strap-grey);
    white-space: nowrap;
  }
</style>
</head>
<body>
<main class="poster">
  <svg class="scenery" viewBox="0 0 850 1200" role="img" aria-label="Photograph of a woman in jeans sitting barefoot on green rolling hills under a clear blue sky, with a lone tree on the right">
    <defs>
      <linearGradient id="sky" x1="0" y1="0" x2="0" y2="1">
        <stop offset="0" stop-color="var(--sky-top)"/>
        <stop offset="0.4" stop-color="var(--sky-mid)"/>
        <stop offset="0.7" stop-color="var(--sky-low)"/>
        <stop offset="0.82" stop-color="var(--sky-horizon)"/>
      </linearGradient>
      <linearGradient id="grass" x1="0" y1="0" x2="0" y2="1">
        <stop offset="0" stop-color="var(--grass-light)"/>
        <stop offset="0.5" stop-color="var(--grass-mid)"/>
        <stop offset="1" stop-color="var(--grass-dark)"/>
      </linearGradient>
      <linearGradient id="portrait" x1="0" y1="0" x2="0" y2="1">
        <stop offset="0" stop-color="var(--portrait-warm)"/>
        <stop offset="1" stop-color="var(--portrait-denim)"/>
      </linearGradient>
    </defs>
    <rect class="scenery__sky" width="850" height="1200" fill="url(#sky)"/>
    <path class="scenery__far-hill" d="M0 985 Q180 955 380 985 Q600 1010 850 955 L850 1200 L0 1200 Z" fill="var(--grass-light)" opacity="0.85"/>
    <path class="scenery__near-hill" d="M0 1000 Q220 975 430 1005 Q640 1030 850 990 L850 1200 L0 1200 Z" fill="url(#grass)"/>
    <rect class="scenery__tree" x="660" y="838" width="140" height="172" rx="70" fill="var(--tree-green)" role="img" aria-label="Lone leafy tree on the hill"/>
    <rect class="scenery__portrait" x="62" y="772" width="242" height="402" rx="60" fill="url(#portrait)" role="img" aria-label="Smiling woman sitting on the grass hugging her knees"/>
  </svg>

  <h1 class="title">60 Ways to De-stress</h1>

  <ul class="ways ways--first">
    <li>Put on some music and dance</li>
    <li>Make a gratitude list</li>
    <li>Eat something mindfully</li>
    <li>Go to the park</li>
    <li>Light a scented candle</li>
    <li>Buy yourself flowers</li>
    <li>Listening to music</li>
    <li>Call or visit a friend</li>
    <li>Take a nap</li>
    <li>Take some deep breaths</li>
    <li>Take a mini mental holiday</li>
    <li>Watch the clouds go by</li>
    <li>Have a bath</li>
    <li>Meditate</li>
    <li>Write in a journal</li>
    <li>Go for a walk</li>
    <li>Plant a tree</li>
    <li>Swing ona  swing</li>
    <li>Forgive someone</li>
    <li>Write a poem</li>
  </ul>

  <ul class="ways ways--second">
    <li>Hug someone</li>
    <li>Fake a smile</li>
    <li>Gaze at the stars</li>
    <li>Play a game</li>
    <li>Stand up and stretch</li>
    <li>Paint a picture</li>
    <li>Read a book</li>
    <li>Look at a work of art</li>
    <li>Bake some cookies</li>
    <li>Go for a bike ride</li>
    <li>Review your achievements</li>
    <li>Relive happy memories</li>
    <li>Get a haircut</li>
    <li>Pat a dog</li>
    <li>Volunteer your time</li>
    <li>Perform  an act of kindness</li>
    <li>Give yourself a time-out</li>
    <li>Make yourself a cup of tea</li>
    <li>Listen to a guided relaxation mp3</li>
    <li>Watch a funny movie</li>
  </ul>

  <ul class="ways ways--third">
    <li>Disconnect from technology</li>
    <li>Colour in</li>
    <li>Play in the Park</li>
    <li>Take a class at the gym</li>
    <li>Get a massage</li>
    <li>De-clutter a drawer</li>
    <li>Take a long drive</li>
    <li>Borrow  a book from the library</li>
    <li>Go on a picnic</li>
    <li>Visit a farmers market</li>
    <li>Vent</li>
    <li>Live for today</li>
    <li>Ask for help</li>
    <li>Create some routines</li>
    <li>Scale down your to do list</li>
    <li>Accept what you can't change</li>
    <li>Compliment yourself often</li>
    <li>Outsource if you can</li>
    <li>Write positive self-statements</li>
    <li>Try Progressive Muscle Relaxation</li>
  </ul>

  <div class="brand">
    <span class="brand__mark" aria-hidden="true"></span>
    <p class="brand__name">Willowbank Haven</p>
    <p class="brand__strap">counselling &amp; coaching for mums</p>
  </div>
</main>
</body>
</html>
```